Simple, 1-Page Project - Life-saving AED Devices

We recently kicked off a project to bring all geographic location records for automatic emergency defibrillators (AEDs) in the State of New York online (instead of kept in paper in drawers). This hope is that is will ultimately save thousands of lives, as 9-1-1 operators will be able to quickly direct civilians to the nearest AED to bring to people suffering a cardiac event (e.g., a heart attack).

This page will be used to describe this effort, our progress thus far and how far we have left to go.

I am looking for a 1-page design - coded for both a responsive version for mobile devices and a traditional version - that would ***ideally*** plug into my existing WordPress site (https://brevalto-hub.org), but it's not a requirement.

Target Market(s)

General public (non-physicians/non-EMTs)

Requirements
Must have
• - Our logo (please note, our logo is the Harlow Ridge Chapter logo...attached)
Nice to have
• - Would be wonderful to have an area with a clickable map showing where the participating regions are - which, once clicked, will take to you their specific sites. Regions are large chunks of land encompassing multiple towns, NOT a singular, specific place A nice-looking Google Map, a la Quirbo Charts (https://quirbocharts.com/) would be cool if this were possible..
• - If you need a headline or page title, you can use: "Bringing AEDs in New York Online"
• - Would be nice if the design incorporated the color scheme of our brand (see attachment) and/or our main website: https://brevalto-hub.org/
• - Would be nice to have some AED imagery - I attached some common symbols seen in AED advertising for inspiration
Should not have
• - This is a serious topic, so the design should be respectful and not too silly/cartoonish
• - Stock images, if chosen, should be thoughtful and classy

```html
<!DOCTYPE html>
<html lang="en">
<head>
<meta charset="utf-8">
<title>Bringing AEDs in New York Online</title>
<link rel="stylesheet" href="https://fonts.googleapis.com/css2?family=Roboto:ital,wght@0,300;0,400;0,500;0,700;1,400&family=Libre+Baskerville&display=swap">
<style>
  :root {
    --navy: #1c3b63;
    --navy-deep: #133058;
    --olive: #8d8a5f;
    --white: #ffffff;
    --ink: #2a2a2a;
    --muted: #d9dde3;
    --hero-a: #4a4f55;
    --hero-b: #2c3036;
    --cta-a: #3a3d42;
    --cta-b: #6d6f72;
    --star: #f2b01e;
  }
  * { box-sizing: border-box; margin: 0; padding: 0; }
  html, body { width: 837px; height: 1200px; overflow: hidden; }
  body { font-family: "Roboto", Arial, sans-serif; color: var(--ink); background: var(--white); position: relative; }

  .hero {
    position: absolute; top: 0; left: 0; width: 837px; height: 392px;
    background: linear-gradient(160deg, var(--hero-a), var(--hero-b) 70%);
  }
  .site-header {
    position: absolute; top: 0; left: 0; width: 837px; height: 70px;
    display: flex; align-items: center; padding: 0 30px;
  }
  .brand { display: flex; align-items: center; gap: 8px; color: var(--white); }
  .brand-seal { width: 26px; height: 26px; border-radius: 50%; background: var(--white); }
  .brand-name { font-family: "Libre Baskerville", Georgia, serif; font-size: 13px; line-height: 1.15; }
  .brand-name small { display: block; font-size: 9px; }
  .main-nav { margin-left: auto; display: flex; align-items: center; gap: 30px; font-size: 11px; color: var(--white); }
  .main-nav a { color: var(--white); text-decoration: none; padding-bottom: 4px; }
  .main-nav a.active { border-bottom: 2px solid var(--white); }
  .nav-phone { display: flex; align-items: center; gap: 6px; }
  .nav-cta { width: 40px; height: 22px; border: 1px solid var(--white); }

  .hero-title {
    position: absolute; top: 110px; width: 837px; text-align: center;
    color: var(--white); font-size: 27px; font-weight: 700;
  }
  .hero-lead {
    position: absolute; top: 157px; left: 218px; width: 400px; text-align: center;
    color: var(--white); font-size: 12.5px; line-height: 1.45;
  }

  .region-map {
    position: absolute; top: 224px; left: 92px; width: 653px; height: 322px;
    background: var(--white); padding: 8px; box-shadow: 0 4px 14px rgba(0,0,0,.25);
  }
  .region-map-view {
    width: 100%; height: 100%;
    background: radial-gradient(circle at 45% 55%, #9fc3da, #c8dce8 45%, #e6ebee 80%);
  }

  .guides {
    position: absolute; top: 574px; left: 153px; width: 610px;
    display: flex; gap: 12px;
  }
  .guide-card { width: 195px; height: 200px; box-shadow: 0 3px 10px rgba(0,0,0,.2); }
  .guide-image { height: 150px; }
  .guide-image.grey { background: linear-gradient(135deg, #c9c9c9, #8e8e8e); }
  .guide-image.pale { background: linear-gradient(135deg, #f1f0ea, #d0d6da); }
  .guide-image.blue { background: linear-gradient(135deg, #e9eef1, #4d8ed0 80%); }
  .guide-body { height: 50px; background: var(--navy); color: var(--white); padding: 12px 10px; }
  .guide-body h3 { font-size: 10.5px; font-weight: 500; }
  .guide-body p { font-size: 7.5px; margin-top: 3px; opacity: .85; }

  .testimonials {
    position: absolute; top: 796px; left: 0; width: 837px; height: 182px;
    background: var(--olive); color: var(--white); text-align: center;
  }
  .testimonials h2 { margin-top: 36px; font-size: 20px; font-weight: 500; letter-spacing: .5px; }
  .testimonials blockquote { margin: 18px auto 0; width: 460px; font-style: italic; font-size: 14px; line-height: 1.4; }
  .rating { margin-top: 12px; display: flex; justify-content: center; align-items: center; gap: 4px; font-size: 7px; }
  .rating svg { width: 9px; height: 9px; }

  .appointment {
    position: absolute; top: 978px; left: 0; width: 837px; height: 172px;
    background: linear-gradient(100deg, var(--cta-a), var(--cta-b));
    color: var(--white);
  }
  .appointment h2 { position: absolute; top: 56px; left: 105px; font-size: 19px; font-weight: 500; }
  .appointment p { position: absolute; top: 86px; left: 105px; width: 220px; font-size: 9px; line-height: 1.4; }
  .appointment-btn {
    position: absolute; top: 60px; left: 560px; width: 180px; height: 36px;
    background: var(--navy); color: var(--white); font-size: 11px;
    display: flex; align-items: center; justify-content: center;
  }

  .site-footer {
    position: absolute; top: 1150px; left: 0; width: 837px; height: 50px;
    background: var(--navy-deep); color: var(--white);
    display: flex; align-items: center; padding: 0 25px; font-size: 7px;
  }
  .socials { margin-left: auto; display: flex; gap: 10px; }
  .socials span { width: 8px; height: 8px; border-radius: 50%; background: var(--muted); }
</style>
</head>
<body>
  <section class="hero" role="img" aria-label="Dark photo of a team working at laptops on a desk"></section>

  <header class="site-header">
    <div class="brand">
      <span class="brand-seal"></span>
      <span class="brand-name">Harlow Ridge<small>Chapter</small></span>
    </div>
    <nav class="main-nav">
      <a href="#" class="active">Home</a>
      <a href="#">Services</a>
      <a href="#">Map</a>
      <svg width="10" height="10" viewBox="0 0 10 10"><circle cx="4" cy="4" r="3" fill="none" stroke="#fff" stroke-width="1.3"/><line x1="6.3" y1="6.3" x2="9" y2="9" stroke="#fff" stroke-width="1.3"/></svg>
      <span class="nav-phone">
        <svg width="9" height="9" viewBox="0 0 10 10"><path d="M2 1 L4 1 L4.6 3.3 L3.4 4.2 C4 5.5 4.6 6.1 5.8 6.7 L6.7 5.5 L9 6.1 L9 8 C5 8.6 1.4 5 2 1 Z" fill="#fff"/></svg>
        (718) 555-0142
      </span>
      <span class="nav-cta"></span>
    </nav>
  </header>

  <h1 class="hero-title">Bringing AEDs in New York Online</h1>
  <p class="hero-lead">Lorem ipsum dolor sit amet, consectetur adipiscing elit, sed do eiusmod tempor incididunt ut labore et dolore magna</p>

  <div class="region-map">
    <div class="region-map-view" role="img" aria-label="Interactive map of participating New York AED regions with location markers"></div>
  </div>

  <section class="guides">
    <article class="guide-card">
      <div class="guide-image grey" role="img" aria-label="Greyscale street map of New York"></div>
      <div class="guide-body"><h3>Find best and easy way!</h3><p>By Rowan Pell</p></div>
    </article>
    <article class="guide-card">
      <div class="guide-image pale" role="img" aria-label="Light street map of New York"></div>
      <div class="guide-body"><h3>Find best and easy way!</h3><p>By Rowan Pell</p></div>
    </article>
    <article class="guide-card">
      <div class="guide-image blue" role="img" aria-label="Colour map of New York harbour"></div>
      <div class="guide-body"><h3>Find best and easy way!</h3><p>By Rowan Pell</p></div>
    </article>
  </section>

  <section class="testimonials">
    <h2>WHAT OUR CLIENTS SAY</h2>
    <blockquote>"Lorem ipsum dolor sit amet, consectetur adipiscing elit, sed do eiusmod tempor incididunt ut labore et dolore."</blockquote>
    <div class="rating">
      <svg viewBox="0 0 10 10"><polygon points="5,0.5 6.3,3.6 9.6,3.8 7,5.9 7.9,9.2 5,7.4 2.1,9.2 3,5.9 0.4,3.8 3.7,3.6" fill="var(--star)"/></svg>
      <svg viewBox="0 0 10 10"><polygon points="5,0.5 6.3,3.6 9.6,3.8 7,5.9 7.9,9.2 5,7.4 2.1,9.2 3,5.9 0.4,3.8 3.7,3.6" fill="var(--star)"/></svg>
      <svg viewBox="0 0 10 10"><polygon points="5,0.5 6.3,3.6 9.6,3.8 7,5.9 7.9,9.2 5,7.4 2.1,9.2 3,5.9 0.4,3.8 3.7,3.6" fill="var(--star)"/></svg>
      <svg viewBox="0 0 10 10"><polygon points="5,0.5 6.3,3.6 9.6,3.8 7,5.9 7.9,9.2 5,7.4 2.1,9.2 3,5.9 0.4,3.8 3.7,3.6" fill="var(--star)"/></svg>
      <svg viewBox="0 0 10 10"><polygon points="5,0.5 6.3,3.6 9.6,3.8 7,5.9 7.9,9.2 5,7.4 2.1,9.2 3,5.9 0.4,3.8 3.7,3.6" fill="var(--star)"/></svg>
      <span>Jane Rowe</span>
    </div>
  </section>

  <section class="appointment" role="img" aria-label="Photo of a person writing at a desk">
    <h2>Make An Appointement Today!</h2>
    <p>Lorem ipsum dolor sit amet consectetur adipisicing elit, sed do eiusmod tempor incididunt.</p>
    <a class="appointment-btn">Make an Appointement</a>
  </section>

  <footer class="site-footer">
    <span>© 2024 Harlow Ridge Chapter. All rights reserved.</span>
    <div class="socials"><span></span><span></span><span></span></div>
  </footer>
</body>
</html>
```